One Pager Website for various security awareness videos

We need a one pager website (design & coding) for our security awareness video series. We imagine placing a few (3-4 sample videos) on the website, a customer referal and some contact form. SOmething similar to https://quorvel.com/watch-now/. Here are some of the videos which we will place on the website:
https://www.streamdeck-example.net/watch?v=Hq7PzkA2mLd&t=112s
https://www.streamdeck-example.net/watch?v=Vb3RkeWn8Ts
https://www.streamdeck-example.net/watch?v=Jw9CdpLr4Ya
https://www.streamdeck-example.net/watch?v=Tz6GyqBn2Kx
https://www.streamdeck-example.net/watch?v=Rm4XhaPe7Qu
https://www.streamdeck-example.net/watch?v=Ed8WokSj3Lf
https://www.streamdeck-example.net/watch?v=Ny2BquTc5Hv
https://www.streamdeck-example.net/watch?v=Pk5FsmVd9Ga
https://www.streamdeck-example.net/watch?v=Wc7JteHn3Rb
As for logo: our company www.tembrashield.com is the creator of those videos. You can use our logo / name.
Target Market(s)
B2B security officers in large enterprises
Coding
Coded - Design and coding required
Number of Pages Required
1 page
Look and feel

```html
<!DOCTYPE html>
<html lang="en">
<head>
<meta charset="utf-8">
<title>Tembra – Watch Episodes</title>
<link href="https://fonts.googleapis.com/css2?family=Poppins:wght@300;400;500;600;700;800&display=swap" rel="stylesheet">
<style>
:root{
  --teal:#00b5bf;
  --orange:#f7931e;
  --orange-deep:#ff8400;
  --ink:#1f1f1f;
  --text:#444;
  --muted:#777;
  --soft:#f3f3f3;
  --row:#efefef;
  --white:#fff;
}
*{box-sizing:border-box;margin:0;padding:0}
html,body{width:1200px;height:3354px;overflow:hidden;background:var(--white)}
body{font-family:'Poppins',sans-serif;color:var(--text);position:relative}
.page{position:relative;width:1200px;height:3354px;overflow:hidden}
.abs{position:absolute}
a{color:inherit;text-decoration:none}

/* top bar */
.topbar{left:91px;top:12px;font-size:12px;color:var(--ink);display:flex;gap:36px;align-items:center}
.topbar span{display:flex;align-items:center;gap:6px}
.topbar-social{right:98px;top:15px;display:flex;gap:34px}
.dot{width:10px;height:10px;border:1.5px solid #555;border-radius:50%}
.topline{left:88px;right:88px;top:36px;height:1px;background:#eee}

/* logo */
.logo{display:flex;align-items:center;gap:8px}
.logo-mark{width:40px;height:40px;border-radius:50%;background:var(--orange)}
.logo-name{font-weight:800;font-size:28px;color:var(--ink);letter-spacing:-.5px}
.header-logo{left:94px;top:56px}

.nav{right:90px;top:66px;display:flex;gap:34px;font-size:12px;font-weight:500;color:var(--ink)}
.nav .active{color:var(--orange);border-bottom:2px solid var(--orange);padding-bottom:3px}

/* hero */
.blob-top{left:690px;top:90px;width:720px;height:700px;border-radius:50%;background:var(--soft)}
.hero-art{left:636px;top:262px;width:564px;height:430px;border-radius:20px;background:linear-gradient(135deg,#fff7e0,#eef0f2)}
.hero-title{left:88px;top:280px;font-size:72px;font-weight:800;color:var(--ink);line-height:1;letter-spacing:1px}
.hero-sub{left:100px;top:362px;font-size:52px;font-weight:400;color:var(--ink);line-height:1}
.btn{display:inline-flex;align-items:center;justify-content:center;border-radius:30px;background:linear-gradient(90deg,var(--orange),var(--orange-deep));color:var(--white);font-weight:700;font-size:13px;text-transform:uppercase;box-shadow:0 6px 14px rgba(247,147,30,.3)}
.hero-btn{left:100px;top:430px;width:170px;height:49px}

.wave{left:0;width:1200px}
.video-circle{left:139px;top:772px;width:456px;height:456px;border-radius:50%;background:radial-gradient(circle,#fff 55%,#f4f4f4);box-shadow:0 20px 40px rgba(0,0,0,.15)}
.play{left:333px;top:966px;width:70px;height:70px;border-radius:50%;background:var(--ink)}
.play svg{position:absolute;left:26px;top:22px}
.stripe-disc{left:89px;top:1080px;width:130px;height:130px;border-radius:50%;background:rgba(255,255,255,.55)}

.latest{left:657px;top:890px;width:455px;color:var(--white)}
.latest h2{font-size:40px;font-weight:800;line-height:1;letter-spacing:.5px}
.latest hr{border:0;border-top:1px solid rgba(255,255,255,.5);margin:12px 0 16px}
.latest .ep{font-size:17px}
.latest .ep b{font-weight:700;margin-left:8px}
.latest p{font-size:14px;line-height:22px;margin-top:16px}
.latest-btn{left:657px;top:1178px;width:133px;height:40px;font-size:12px}

/* seasons */
.seasons{left:260px;top:1414px;width:681px}
.season{height:66px;background:var(--row);border-radius:3px;margin-bottom:10.5px;display:flex;align-items:center;justify-content:space-between;padding:0 24px 0 41px;font-size:24px;color:var(--ink)}
.season b{font-weight:700;margin-left:12px}
.plus{width:28px;height:28px;border-radius:50%;background:var(--white);color:var(--orange);font-size:18px;display:flex;align-items:center;justify-content:center;font-weight:600}

/* testimonial */
.blob-mid{left:990px;top:1740px;width:500px;height:480px;border-radius:50%;background:var(--soft)}
.quote{left:88px;top:1955px;width:460px;font-size:23px;line-height:36px;color:var(--ink)}
.quote-rule{left:88px;top:2128px;width:450px;height:1px;background:#ddd}
.cite{left:88px;top:2150px;font-size:13px;color:var(--ink)}
.cite b{color:var(--orange);font-weight:700}
.meeting-art{left:601px;top:1891px;width:508px;height:348px;border-radius:14px;background:linear-gradient(135deg,#3a3a3a,#e8e8e8)}

/* contact */
.ring-orange{left:787px;top:2280px}
.contact-title{left:88px;top:2470px;font-size:42px;font-weight:800;color:var(--white);letter-spacing:.5px}
.field{position:absolute;height:39px;background:var(--white);border-radius:2px;font-size:12px;color:var(--muted);padding:0 16px;display:flex;align-items:center}
.label{position:absolute;font-size:12px;color:var(--white);font-weight:600}
.note{position:absolute;font-size:12px;color:var(--white);font-weight:500}
.check{position:absolute;font-size:12px;color:var(--white);display:flex;align-items:center;gap:6px}
.check i{width:10px;height:10px;border:1px solid var(--white);border-radius:2px;display:inline-block}
.form-btn{left:88px;top:2877px;width:134px;height:40px;font-size:12px}
.vrule{left:681px;top:2558px;width:1px;height:300px;background:rgba(255,255,255,.35)}
.info{position:absolute;left:750px;display:flex;gap:14px;color:var(--white)}
.info .ic{width:30px;height:30px;border-radius:50%;background:rgba(255,255,255,.25);flex:none;display:flex;align-items:center;justify-content:center;margin-top:4px}
.info h4{font-size:13px;font-weight:700;letter-spacing:.3px}
.info p{font-size:16px;line-height:20px;font-weight:500}
.bigword{left:833px;top:2862px;font-size:150px;font-weight:800;color:var(--white);line-height:1;letter-spacing:2px}

/* footer */
.footer-logo{left:134px;top:3094px}
.f-social{left:122px;top:3168px;display:flex;gap:9px}
.f-social span{width:32px;height:32px;border-radius:50%;background:#f1f1f1}
.fcol{position:absolute;top:3068px}
.fcol h5{font-size:14px;font-weight:700;color:var(--ink);letter-spacing:.5px;margin-bottom:16px}
.fcol a{display:block;font-size:11.5px;color:#666;line-height:26.7px;text-transform:uppercase}
.frule{left:88px;right:88px;top:3300px;height:1px;background:#e5e5e5}
.copy{left:0;width:1200px;top:3316px;text-align:center;font-size:11.5px;color:var(--ink)}
.totop{left:1131px;top:3281px;width:34px;height:34px;border-radius:50%;background:var(--teal);display:flex;align-items:center;justify-content:center}
</style>
</head>
<body>
<div class="page">

  <!-- header -->
  <div class="abs topbar">
    <span><svg width="11" height="11" viewBox="0 0 24 24"><path fill="#333" d="M6.6 10.8a15 15 0 0 0 6.6 6.6l2.2-2.2a1 1 0 0 1 1-.25 11.4 11.4 0 0 0 3.6.57 1 1 0 0 1 1 1V20a1 1 0 0 1-1 1A17 17 0 0 1 3 4a1 1 0 0 1 1-1h3.5a1 1 0 0 1 1 1c0 1.25.2 2.45.57 3.57a1 1 0 0 1-.25 1z"/></svg>+08 123 456 7890</span>
    <span><svg width="11" height="9" viewBox="0 0 24 18"><path fill="#333" d="M0 0h24v18H0zM2 2l10 7 10-7"/></svg>info@example.com</span>
  </div>
  <div class="abs topbar-social"><span class="dot"></span><span class="dot"></span><span class="dot"></span><span class="dot"></span></div>
  <div class="abs topline"></div>

  <div class="abs logo header-logo"><span class="logo-mark"></span><span class="logo-name">Tembra</span></div>
  <nav class="abs nav">
    <a class="active" href="#">WATCH EPISODES</a>
    <a href="#">MARLOW INSIGHTS ▾</a>
    <a href="#">SOLUTIONS ▾</a>
    <a href="#">DELIVERYRESOURCES ▾</a>
    <a href="#">GET PRICING</a>
  </nav>

  <!-- hero -->
  <div class="abs blob-top"></div>
  <div class="abs hero-art" role="img" aria-label="Hand-drawn mascot beside the Tembra name, a laptop sketch and a hand writing with a marker"></div>
  <h1 class="abs hero-title">WATCH TEMBRA</h1>
  <div class="abs hero-sub">SEASON LINEUP</div>
  <a class="abs btn hero-btn" href="#">Watch Episodes</a>

  <svg class="abs wave" style="top:600px" width="1200" height="712" viewBox="0 600 1200 712">
    <path fill="#00b5bf" d="M0,683 C120,760 240,792 360,762 C520,722 640,620 860,612 C1000,608 1120,680 1200,755 L1200,1312 L0,1312Z"/>
  </svg>

  <div class="abs stripe-disc" role="img" aria-label="Striped decorative disc"></div>
  <div class="abs video-circle" role="img" aria-label="Video still: sketched presenter pointing at a clean desk policy board"></div>
  <div class="abs play"><svg width="20" height="26" viewBox="0 0 20 26"><path fill="#fff" d="M0 0l20 13L0 26z"/></svg></div>

  <div class="abs latest">
    <h2>ONE OF OUR LATEST<br>EPISODES</h2>
    <hr>
    <div class="ep">SEASON 6 | EPISODE 4 <b>DON'T FALL FOR IT</b></div>
    <p>Aenean sollicitudin lorem quis bibendum auctor nisi elit ipsum, nec sagittis sem nibh id elit duis sed odio sit amet nibh cursus a sit amet mauris. Morbi accumsan ipsum velit. Nam odio quat auctor eu in elit. Class aptent taciti sociosqu ad litora torquent per conubia nostra per inceptos himenaeos.</p>
  </div>
  <a class="abs btn latest-btn" href="#">Get Pricing</a>

  <!-- seasons -->
  <div class="abs seasons">
    <div class="season"><span>2021 - <b>SEASON 6</b></span><span class="plus">+</span></div>
    <div class="season"><span>2020 - <b>SEASON 5</b></span><span class="plus">+</span></div>
    <div class="season"><span>2019 - <b>SEASON 4</b></span><span class="plus">+</span></div>
    <div class="season"><span>2018 - <b>SEASON 3</b></span><span class="plus">+</span></div>
    <div class="season"><span>2017 - <b>SEASON 2</b></span><span class="plus">+</span></div>
  </div>

  <!-- testimonial -->
  <div class="abs blob-mid"></div>
  <blockquote class="abs quote">The cybersecurity videos are fast, fun, and easy to distribute to employees. We've seen click-through rates on spam test emails drop rapidly.</blockquote>
  <div class="abs quote-rule"></div>
  <div class="abs cite"><b>— ACCOUNTING DIRECTOR IN GOVERNMENT</b> | 50M – 250M USD</div>
  <div class="abs meeting-art" role="img" aria-label="Sketch of a laptop showing a video call with several participants"></div>

  <!-- contact -->
  <svg class="abs wave" style="top:2290px" width="1200" height="690" viewBox="0 2290 1200 690">
    <path fill="#00b5bf" d="M0,2447 C150,2340 300,2300 450,2310 C650,2325 800,2470 960,2470 C1080,2470 1150,2420 1200,2382 L1200,2980 L0,2980Z"/>
  </svg>
  <svg class="abs ring-orange" width="256" height="214" viewBox="0 0 256 214" role="img" aria-label="Orange striped decorative disc">
    <defs><clipPath id="discClip"><rect x="0" y="0" width="256" height="214"/></clipPath></defs>
    <circle cx="128" cy="128" r="128" fill="#f7931e" opacity=".85" clip-path="url(#discClip)"/>
  </svg>

  <h2 class="abs contact-title">SPEAK WITH AN EXPERT</h2>
  <div class="field" style="left:88px;top:2542px;width:239px">First name*</div>
  <div class="field" style="left:336px;top:2542px;width:238px">Last name*</div>
  <div class="field" style="left:88px;top:2592px;width:239px">Business email*</div>
  <div class="field" style="left:336px;top:2592px;width:238px">Company name*</div>
  <div class="field" style="left:88px;top:2642px;width:239px">Company size*</div>
  <div class="field" style="left:336px;top:2642px;width:238px">How did you hear about tembra*</div>
  <div class="label" style="left:88px;top:2699px">Best contact number to reach you*</div>
  <div class="field" style="left:88px;top:2722px;width:486px">Best phone number to reach you</div>
  <div class="note" style="left:88px;top:2784px">Provide an accurate user count to ensure the correct TEMBRA representative is assigned.</div>
  <div class="check" style="left:88px;top:2815px"><i></i>Click here if you'd like pricing information</div>
  <div class="check" style="left:88px;top:2835px"><i></i>I am interested in reselling TEMBRA</div>
  <a class="abs btn form-btn" href="#">Get Pricing</a>

  <div class="abs vrule"></div>
  <div class="info" style="top:2585px"><span class="ic"><svg width="10" height="14" viewBox="0 0 10 14"><path fill="#fff" d="M5 0a5 5 0 0 1 5 5c0 4-5 9-5 9S0 9 0 5a5 5 0 0 1 5-5zm0 3a2 2 0 1 0 0 4 2 2 0 0 0 0-4z"/></svg></span><div><h4>LOCATION</h4><p>Some address line goes here city name<br>country name goes here</p></div></div>
  <div class="info" style="top:2666px"><span class="ic"><svg width="12" height="12" viewBox="0 0 24 24"><path fill="#fff" d="M6.6 10.8a15 15 0 0 0 6.6 6.6l2.2-2.2a1 1 0 0 1 1-.25 11.4 11.4 0 0 0 3.6.57 1 1 0 0 1 1 1V20a1 1 0 0 1-1 1A17 17 0 0 1 3 4a1 1 0 0 1 1-1h3.5a1 1 0 0 1 1 1c0 1.25.2 2.45.57 3.57a1 1 0 0 1-.25 1z"/></svg></span><div><h4>PHONE</h4><p>800-555-0142</p></div></div>
  <div class="info" style="top:2724px"><span class="ic"><svg width="12" height="9" viewBox="0 0 24 18"><path fill="#fff" d="M0 0h24v18H0z"/></svg></span><div><h4>EMAIL</h4><p>info@example.com.au</p></div></div>
  <div class="info" style="top:2791px"><span class="ic"><svg width="12" height="12" viewBox="0 0 24 24"><circle cx="12" cy="12" r="11" fill="#fff"/><path d="M12 6v6l4 3" stroke="#00b5bf" stroke-width="2.5" fill="none"/></svg></span><div><h4>OPENING HOURS</h4><p>MONDAY - SUNDAY: 8:30 AM - 6:00 PM</p></div></div>
  <div class="abs bigword">TEMBRA</div>
  <div class="abs" style="left:0;top:2980px;width:1200px;height:374px;background:#fff"></div>

  <!-- footer -->
  <div class="abs logo footer-logo"><span class="logo-mark"></span><span class="logo-name">Tembra</span></div>
  <div class="abs f-social"><span></span><span></span><span></span><span></span></div>
  <div class="fcol" style="left:377px"><h5>NAVIGATE</h5><a href="#">About</a><a href="#">Partnerships</a><a href="#">Blog</a><a href="#">Contact</a><a href="#">Free Trial</a></div>
  <div class="fcol" style="left:531px"><h5>SOLUTIONS</h5><a href="#">Tembra Aware Anime</a><a href="#">Tembra Aware Corporate</a><a href="#">Tembra Aware Enterprise</a></div>
  <div class="fcol" style="left:750px"><h5>COMPLIANCE</h5><a href="#">Tembra PCI</a><a href="#">Tembra HIPAA</a><a href="#">Tembra GDPR</a><a href="#">Tembra CCPA</a></div>
  <div class="fcol" style="left:921px"><h5>COMMUNITY</h5><a href="#">Tembra Family</a><a href="#">Tembra K-12 + University</a><a href="#">Tembra Security for Good</a></div>
  <div class="abs frule"></div>
  <div class="abs copy">© COPYRIGHT 2021 TEMBRA, LLC. ALL RIGHTS RESERVED.</div>
  <a class="abs totop" href="#"><svg width="10" height="12" viewBox="0 0 10 12"><path d="M5 11V1M1 5l4-4 4 4" stroke="#fff" stroke-width="1.4" fill="none"/></svg></a>

</div>
</body>
</html>
```